US Higher Education Changes Infographic

Create an info graphic which visually demonstrates statistics from and industry study of college students/parents and higher education professionals.

This graphic should be visually pleasing and conform with our brand styles.

Illustrations/icons should not be too juvenile or cartoon

We prefer a vibrant crisp design and is impactful and not cluttered.

examples are attached for reference.

Target Market(s)

US higher education industry

Industry/Entity Type

College

Requirements
Must have
• 8x10 finished design
• use colors and fonts from style guide
Should not have
• cluttered design, juvenile images

```html
<!DOCTYPE html>
<html lang="en">
<head>
<meta charset="utf-8">
<title>The FAFSA Opens Early</title>
<link rel="stylesheet" href="https://fonts.googleapis.com/css2?family=Montserrat:wght@400;500;600;700&family=Oswald:wght@400&display=swap">
<style>
:root{
  --green:#62b440;
  --orange:#f7941d;
  --ink:#222222;
  --panel:#f2f2f2;
  --octagon:#ececec;
  --white:#ffffff;
}
*{margin:0;padding:0;box-sizing:border-box}
html,body{width:960px;height:1200px;overflow:hidden;background:var(--white)}
body{font-family:"Montserrat",sans-serif;color:var(--ink)}
.canvas{position:relative;width:960px;height:1200px;overflow:hidden}
.abs{position:absolute}

.masthead{left:0;top:0;width:960px;height:178px;background:var(--green);text-align:center;color:var(--white)}
.masthead h1{font-weight:700;font-size:41px;letter-spacing:.5px;padding-top:26px}
.masthead p{font-weight:400;font-size:19px;letter-spacing:1.5px;line-height:26px;margin-top:16px;text-transform:uppercase}

.section-title{font-weight:700;font-size:18px;color:var(--green);letter-spacing:.2px;white-space:nowrap}
.rule{height:4px;background:var(--ink)}
.intro{font-size:15.5px;line-height:23px;font-weight:500;white-space:nowrap}
.intro .big{color:var(--orange);font-weight:700;font-size:22px}

.banner-label{color:var(--white);font-weight:600;font-size:18px;letter-spacing:.3px;white-space:nowrap}

.stat{font-family:"Oswald",sans-serif;color:var(--orange);font-weight:400;font-size:56px;line-height:1;letter-spacing:-.5px;white-space:nowrap}
.note{font-size:14.5px;line-height:20.5px;font-weight:500;white-space:nowrap}

.panel{background:var(--panel);border-radius:14px}
.panel-title{position:absolute;left:0;width:100%;text-align:center;font-weight:600;font-size:18px;letter-spacing:.3px}

.artwork{background:linear-gradient(180deg,#3a3a3a,#111111);border-radius:6px}

.practices li{list-style:none;font-size:15.5px;line-height:22px;font-weight:500;position:absolute;left:162px;white-space:nowrap}

.footer{left:0;top:1109px;width:960px;height:91px;background:var(--green);color:var(--white)}
.footer .credit{position:absolute;left:238px;top:22px;font-weight:700;font-size:15.5px;letter-spacing:.3px;white-space:nowrap}
.footer .small{position:absolute;left:321px;top:50px;font-size:10.5px;font-weight:400;white-space:nowrap}
.brand{position:absolute;left:500px;top:27px;display:flex;align-items:center;gap:10px;font-weight:600;font-size:28px}
.brand i{display:block;width:30px;height:30px;border-radius:50%;background:var(--white)}
</style>
</head>
<body>
<div class="canvas">

  <header class="masthead abs">
    <h1>THE FAFSA OPENS EARLY</h1>
    <p>The class of 2017 will begin filing their FAFSA on<br>October 1st using income and tax data from 2015</p>
  </header>

  <h2 class="section-title abs" style="left:41px;top:221px">WHAT ARE STUDENTS AND FAMILIES SAYING?</h2>
  <div class="rule abs" style="left:41px;top:244px;width:462px"></div>
  <p class="intro abs" style="left:41px;top:260px">Of students who plan to aid for financial aid, <span class="big">76%</span><br>indicated that cost was an important factor in the<br>college selection process.&nbsp; More specifically, students<br>and families want:</p>

  <h2 class="section-title abs" style="left:541px;top:221px">HOW ARE COLLEGES RESPONDING?</h2>
  <div class="rule abs" style="left:541px;top:244px;width:390px"></div>
  <p class="intro abs" style="left:550px;top:260px">Of the colleges polled in this study, <span class="big">89%</span><br>think changes will have a significant or<br>VERY significant impact on the admissions<br>cycle. As a result, colleges are:</p>

  <!-- Row 1 -->
  <svg class="abs" style="left:31px;top:385px" width="330" height="40"><polygon points="0,0 330,0 306,40 0,40" fill="var(--green)"/></svg>
  <div class="banner-label abs" style="left:53px;top:394px">EARLIER UNDERSTANDING</div>
  <svg class="abs" style="left:41px;top:425px" width="116" height="90"><polygon points="33,0 83,0 116,27 116,63 83,90 33,90 0,63 0,27" fill="var(--octagon)"/></svg>
  <div class="stat abs" style="left:44px;top:436px">69%</div>
  <p class="note abs" style="left:166px;top:428px">believe an earlier<br>understanding of cost and<br>aid would be helpful to<br>their planning process</p>
  <div class="artwork abs" role="img" aria-label="Graduation cap above a large question mark" style="left:378px;top:372px;width:84px;height:143px"></div>

  <svg class="abs" style="left:488px;top:406px" width="62" height="88"><polygon points="0,0 62,44 0,88" fill="var(--green)"/></svg>
  <div class="panel abs" style="left:535px;top:381px;width:393px;height:142px">
    <div class="panel-title" style="top:12px">PLANNING TO CHANGE</div>
    <div class="stat abs" style="left:25px;top:52px">68.4%</div>
    <p class="note abs" style="left:171px;top:50px">plan to make significant<br>changes as a result of PPY<br>and early FAFSA in 2016.</p>
  </div>

  <!-- Row 2 -->
  <svg class="abs" style="left:31px;top:535px" width="420" height="40"><polygon points="0,0 420,0 396,40 0,40" fill="var(--green)"/></svg>
  <div class="banner-label abs" style="left:46px;top:544px">EARLIER AWARD LETTER DELIVERY</div>
  <div class="stat abs" style="left:31px;top:584px">88.6%</div>
  <p class="note abs" style="left:194px;top:595px">want their award<br>letter earlier .</p>
  <p class="note abs" style="left:46px;top:656px">41% want their award letter in the fall<br>semester of their Senior Year</p>
  <div class="artwork abs" role="img" aria-label="Two award letter documents" style="left:338px;top:583px;width:122px;height:108px"></div>

  <svg class="abs" style="left:488px;top:575px" width="62" height="82"><polygon points="0,0 62,41 0,82" fill="var(--green)"/></svg>
  <div class="panel abs" style="left:535px;top:540px;width:393px;height:162px">
    <div class="panel-title" style="top:30px">DELIVERING EARLIER INSIGHTS</div>
    <div class="stat abs" style="left:40px;top:70px">77%</div>
    <p class="note abs" style="left:156px;top:66px">plan to shift their delivery<br>of financial aid eligibility<br>information earlier</p>
  </div>

  <!-- Row 3 -->
  <svg class="abs" style="left:31px;top:735px" width="310" height="40"><polygon points="0,0 310,0 286,40 0,40" fill="var(--green)"/></svg>
  <div class="banner-label abs" style="left:50px;top:744px">MORE TRANSPARENCY</div>
  <svg class="abs" style="left:41px;top:775px" width="116" height="112"><polygon points="33,0 83,0 116,32 116,80 83,112 33,112 0,80 0,32" fill="var(--octagon)"/></svg>
  <div class="stat abs" style="left:44px;top:786px">82%</div>
  <p class="note abs" style="left:163px;top:788px">would think more positively<br>about a college that<br>provided earlier insight</p>
  <div class="artwork abs" role="img" aria-label="Silhouette of a presenter holding a pointer" style="left:376px;top:722px;width:78px;height:176px"></div>

  <svg class="abs" style="left:488px;top:778px" width="62" height="84"><polygon points="0,0 62,42 0,84" fill="var(--green)"/></svg>
  <div class="panel abs" style="left:535px;top:731px;width:393px;height:176px">
    <div class="panel-title" style="top:20px">CONSEQUENCES OF INACTION</div>
    <div class="stat abs" style="left:27px;top:72px">80%</div>
    <p class="note abs" style="left:140px;top:58px">believe that institutions that<br>DO NOT shift their cycle earlier<br>will be at a competitive<br>disadvantage</p>
  </div>

  <!-- Best practices -->
  <h2 class="section-title abs" style="left:41px;top:940px">EMERGING BEST PRACTICES:</h2>
  <div class="rule abs" style="left:41px;top:966px;width:890px"></div>

  <svg class="abs" style="left:98px;top:988px" width="40" height="94">
    <g fill="none" stroke="var(--orange)" stroke-width="2">
      <rect x="2" y="8" width="24" height="20" rx="3"/>
      <rect x="2" y="38" width="24" height="20" rx="3"/>
      <rect x="2" y="68" width="24" height="20" rx="3"/>
    </g>
    <g fill="none" stroke="var(--orange)" stroke-width="4" stroke-linecap="round" stroke-linejoin="round">
      <polyline points="7,17 14,24 33,3"/>
      <polyline points="7,47 14,54 33,33"/>
      <polyline points="7,77 14,84 33,63"/>
    </g>
  </svg>
  <ul class="practices">
    <li style="top:992px">1. Address ‘the cost question’ earlier in outreach and nurturing campaigns.</li>
    <li style="top:1014px">2. Communicate cost alongside personalized value content</li>
    <li style="top:1036px">3. Extend communications programs to nurture relationships with prospective students<br>along the way.</li>
  </ul>

  <footer class="footer abs">
    <div class="credit">INFOGRAPHIC PROVIDED BY:</div>
    <div class="small">*Black icons by Iconfield</div>
    <div class="brand"><i></i>Veridane</div>
  </footer>

</div>
</body>
</html>
```